Australian Software Consultancy needs new Business Card Design

Design Business Card based on existing design artefacts (attached). We are open to all designs. As its a 2 sided design and we thought it might be quite striking to have one side with a black background and te other side with a white background.

Target Market(s)

Financial Services mainly.

Industry/Entity Type

Business

Contact Information for Business Card

Name :
Position :
Email :

Requirements
Must have
• Funky design using our existing assets

```html
<!DOCTYPE html>
<html lang="en">
<head>
<meta charset="utf-8">
<title>Kestrel Point – Business Card</title>
<link href="https://fonts.googleapis.com/css2?family=Oswald:wght@500&family=Montserrat:wght@400;500&display=swap" rel="stylesheet">
<style>
  :root {
    --backdrop: #3b3b3b;
    --backdrop-dark: #262626;
    --card: #050505;
    --ink: #ffffff;
    --accent: #e3262b;
    --divider: #cfcfcf;
  }
  * { box-sizing: border-box; margin: 0; padding: 0; }
  html, body { width: 1200px; height: 864px; overflow: hidden; }
  body {
    background: radial-gradient(ellipse at center, var(--backdrop) 0%, var(--backdrop-dark) 100%);
    font-family: "Montserrat", sans-serif;
    position: relative;
  }
  .card {
    position: absolute;
    left: 340px;
    width: 520px;
    height: 298px;
    background: var(--card);
    box-shadow: 0 10px 30px rgba(0,0,0,0.55);
  }
  .card--front { top: 110px; }
  .card--back { top: 456px; }

  .brand {
    position: absolute;
    inset: 0;
    display: flex;
    align-items: center;
    justify-content: center;
    gap: 14px;
  }
  .brand__dot {
    width: 46px; height: 46px;
    border-radius: 50%;
    border: 6px solid var(--accent);
  }
  .brand__name {
    font-family: "Oswald", sans-serif;
    font-weight: 500;
    font-size: 30px;
    letter-spacing: 1px;
    color: var(--accent);
    text-transform: uppercase;
  }

  .identity {
    position: absolute;
    top: 108px;
    left: 66px;
    display: flex;
    align-items: center;
  }
  .identity__person { text-align: right; padding-right: 14px; }
  .identity__name {
    font-family: "Oswald", sans-serif;
    font-weight: 500;
    font-size: 30px;
    line-height: 1;
    color: var(--ink);
    text-transform: uppercase;
  }
  .identity__role {
    font-size: 13px;
    color: var(--accent);
    margin-top: 2px;
  }
  .identity__divider {
    width: 1px; height: 50px;
    background: var(--divider);
  }
  .contact { list-style: none; padding-left: 12px; }
  .contact__item {
    display: flex; align-items: center; gap: 7px;
    font-size: 12.5px; color: var(--ink); line-height: 18px;
  }
  .contact__icon { width: 11px; height: 11px; fill: var(--accent); flex: none; }
  .address {
    position: absolute;
    bottom: 56px; left: 0; right: 0;
    text-align: center;
    font-size: 13px;
    color: var(--ink);
  }
</style>
</head>
<body>
  <section class="card card--front" aria-label="Card front">
    <div class="brand">
      <span class="brand__dot"></span>
      <span class="brand__name">Kestrel Point</span>
    </div>
  </section>

  <section class="card card--back" aria-label="Card back">
    <div class="identity">
      <div class="identity__person">
        <div class="identity__name">Daniel Harrow</div>
        <div class="identity__role">President</div>
      </div>
      <div class="identity__divider"></div>
      <ul class="contact">
        <li class="contact__item">
          <svg class="contact__icon" viewBox="0 0 24 24"><path d="M6.6 10.8a15.1 15.1 0 0 0 6.6 6.6l2.2-2.2a1 1 0 0 1 1-.25 11.4 11.4 0 0 0 3.6.57 1 1 0 0 1 1 1V20a1 1 0 0 1-1 1A17 17 0 0 1 3 4a1 1 0 0 1 1-1h3.5a1 1 0 0 1 1 1c0 1.25.2 2.45.57 3.6a1 1 0 0 1-.25 1z"/></svg>
          012-555-0147
        </li>
        <li class="contact__item">
          <svg class="contact__icon" viewBox="0 0 24 24"><path d="M2 5h20v14H2z" opacity=".0"/><path d="M2 6l10 7 10-7v12H2z"/><path d="M2 5h20l-10 7z"/></svg>
          info@kestrelpoint.com
        </li>
        <li class="contact__item">
          <svg class="contact__icon" viewBox="0 0 24 24"><path d="M12 2a10 10 0 1 0 0 20 10 10 0 0 0 0-20zm6.9 6h-2.9a15.7 15.7 0 0 0-1.4-3.6A8 8 0 0 1 18.9 8zM12 4c.8 1.2 1.5 2.5 1.9 4h-3.8c.4-1.5 1.1-2.8 1.9-4zM4.3 14a8 8 0 0 1 0-4h3.4a16 16 0 0 0 0 4zm.8 2h2.9c.3 1.3.8 2.5 1.4 3.6A8 8 0 0 1 5.1 16zM8 8H5.1a8 8 0 0 1 4.3-3.6C8.8 5.5 8.3 6.7 8 8zm4 12c-.8-1.2-1.5-2.5-1.9-4h3.8c-.4 1.5-1.1 2.8-1.9 4zm2.3-6H9.7a14.7 14.7 0 0 1 0-4h4.6a14.7 14.7 0 0 1 0 4zm.3 5.6c.6-1.1 1.1-2.3 1.4-3.6h2.9a8 8 0 0 1-4.3 3.6zm1.7-5.6a16 16 0 0 0 0-4h3.4a8 8 0 0 1 0 4z"/></svg>
          www.kestrelpoint.com
        </li>
      </ul>
    </div>
    <p class="address">Street Name, Suite 100, State, Zip Code, Country</p>
  </section>
</body>
</html>
```